Lark and Fern: Prespective and Balence in People's Lives Needs a Buissness Card Design

Lark and Fern Community Center is an organization that seeks to bring balance into people's lives. Main services include: guided meditation, group brainstorming, and guided counseling. Lark and Fern combines Eastern practices, i.e. Buddhism, Hinduism, and Taoism, with Western practices: therapy, group brainstorming and healing. We would like a double sided card: 1) front vertical with image, 2) back horizontal with information. The main colors for the card are red, white, black. Different finishes would be nice--please no high gloss. Matte, pearlized, embossing--used tactfully and sparingly would be nice. The card should convey balance/harmony in a modern world.

```html
<!DOCTYPE html>
<html lang="en">
<head>
<meta charset="utf-8">
<title>Lark and Fern – Business Card</title>
<link rel="stylesheet" href="https://fonts.googleapis.com/css2?family=Roboto:wght@300;400&display=swap">
<style>
  :root {
    --canvas: #e9e6e1;
    --ink: #000000;
    --paper: #ffffff;
    --paper-shade: #ececec;
    --accent: #e0202c;
    --frame: #bdbdbd;
    --text-light: #f2f2f2;
  }
  * { margin: 0; padding: 0; box-sizing: border-box; }
  html, body { width: 1200px; height: 886px; overflow: hidden; }
  body {
    background: var(--canvas);
    font-family: "Roboto", Arial, sans-serif;
    position: relative;
  }

  /* Back card – horizontal, information side */
  .card-back {
    position: absolute;
    left: 60px; top: 278px;
    width: 580px; height: 330px;
    background: var(--ink);
    border-radius: 18px;
    padding: 14px;
  }
  .card-back__frame {
    width: 100%; height: 100%;
    border: 1px solid var(--frame);
    border-radius: 14px;
    color: var(--text-light);
    padding: 38px 40px 28px 46px;
    display: flex;
    flex-direction: column;
  }
  .brand-name {
    font-size: 34px; font-weight: 400; line-height: 1; letter-spacing: 0.2px;
  }
  .brand-tagline {
    font-size: 14px; font-weight: 300; margin-top: 8px;
  }
  .employee {
    margin-top: 26px; margin-left: 110px;
  }
  .employee__name { font-size: 21px; font-weight: 400; line-height: 1; }
  .employee__position { font-size: 11px; font-weight: 300; margin-top: 3px; margin-left: 70px; }
  .contact {
    list-style: none;
    margin-top: 22px; margin-left: 220px;
    font-size: 12.5px; font-weight: 300; line-height: 1.45;
  }
  .contact li:nth-child(2) { margin-left: 30px; }
  .contact li:nth-child(3) { margin-left: 10px; }
  .contact li:nth-child(4) { margin-left: 55px; }
  .address {
    margin-top: auto; margin-left: 60px;
    font-size: 13px; font-weight: 300;
  }

  /* Front card – vertical, image side */
  .card-front {
    position: absolute;
    left: 770px; top: 146px;
    width: 340px; height: 595px;
    border-radius: 18px;
    overflow: hidden;
    background: linear-gradient(90deg, var(--paper) 0%, var(--paper-shade) 58%, var(--ink) 58%, var(--ink) 100%);
  }
  .card-front__mark {
    position: absolute;
    left: 50%; top: 220px;
    transform: translateX(-50%);
    display: flex; flex-direction: column; align-items: center;
  }
  .mark-circle {
    width: 150px; height: 150px; border-radius: 50%;
    background: var(--accent);
  }
  .card-front__name {
    position: absolute;
    left: 22px; top: 420px;
    font-size: 22px; font-weight: 400; color: var(--ink);
  }
</style>
</head>
<body>
  <section class="card-back" aria-label="Business card, information side">
    <div class="card-back__frame">
      <h1 class="brand-name">Lark and Fern</h1>
      <p class="brand-tagline">Prespective and Balence in People's Lives</p>
      <div class="employee">
        <p class="employee__name">Employee Name</p>
        <p class="employee__position">Your Position</p>
      </div>
      <ul class="contact">
        <li>www.yourwebsite.com</li>
        <li>012 345 6789</li>
        <li>info@youremail.com</li>
        <li>Your Blog.com</li>
      </ul>
      <p class="address">Your Adress Inc 2nd Lane Ave Edison, NJ 00000</p>
    </div>
  </section>

  <section class="card-front" aria-label="Business card, image side">
    <div class="card-front__mark">
      <span class="mark-circle"></span>
    </div>
    <p class="card-front__name">Lark and Fern</p>
  </section>
</body>
</html>
```